Tolvern Business Cards

Business card design. dont mind if new logo is suggested.
it would be for a security company.
our clients would be bigger security companies around Australia.
have a logo done but can be replaced. see attaached. like the colors.
Need company name, person name, designation, phone and email on front.
At back company logo and name. website saddress and 2 x license numbers
would like to have 2 different background color for both sidde

Industry/Entity Type

Security

Contact Information for Business Card

round corners, front should be light in color. need logo at back with webaddress and 2 x license numners

Font styles to use
Sans Serif

Colors
f37122
faa54b
f8ba93
0255a3
0592cd
85cae6
b3d448
9bcb3c
ffffff

Requirements
Must have
• see description
Nice to have
• see description
Should not have
• should not be difficult to read or hardd to find information on card.. lets say easy on eyes yet catchy

```html
<!DOCTYPE html>
<html lang="en">
<head>
<meta charset="utf-8">
<title>Tolvern Security Group – Business Cards</title>
<link href="https://fonts.googleapis.com/css2?family=Source+Sans+3:wght@400;600;700&display=swap" rel="stylesheet">
<style>
  :root {
    --navy: #00147f;
    --title-blue: #0b1f8f;
    --ink: #111111;
    --card-white: #ffffff;
    --stage-light: #dcdcdc;
    --stage-dark: #b0b0b0;
  }
  * { margin: 0; padding: 0; box-sizing: border-box; }
  html, body { width: 1200px; height: 1200px; overflow: hidden; }
  body {
    position: relative;
    font-family: "Source Sans 3", sans-serif;
    background: radial-gradient(ellipse at 50% 50%, var(--stage-light) 0%, var(--stage-dark) 70%);
  }
  .card {
    position: absolute;
    left: 216px;
    width: 796px;
    height: 453px;
    overflow: hidden;
  }
  /* Front */
  .card-front {
    top: 135px;
    background: var(--card-white);
    border-radius: 0 46px 0 46px;
  }
  .front-band {
    position: absolute;
    left: 0; right: 0; bottom: 0;
    height: 51px;
    background: var(--navy);
  }
  .front-brand {
    position: absolute;
    left: 84px; top: 140px;
    width: 220px;
    display: flex; align-items: center; justify-content: center; gap: 12px;
    color: var(--navy);
    font-size: 46px; font-weight: 700;
  }
  .brand-square {
    width: 22px; height: 22px;
    background: currentColor;
  }
  .contact {
    position: absolute;
    left: 398px; top: 40px;
    color: var(--ink);
  }
  .person-name { font-size: 32px; font-weight: 700; line-height: 1.1; }
  .person-title { font-size: 24px; color: var(--title-blue); margin-top: 4px; }
  .detail-list { list-style: none; margin-top: 30px; font-size: 23px; line-height: 30px; }
  .detail-list li { display: flex; }
  .detail-list .label { width: 38px; flex: none; }
  .detail-list .gap { margin-top: 22px; }
  .detail-list .gap-lg { margin-top: 23px; }
  /* Back */
  .card-back {
    top: 614px;
    background: var(--navy);
    border-radius: 46px 0 46px 0;
    color: var(--card-white);
    text-align: center;
  }
  .back-brand {
    position: absolute;
    left: 0; right: 0; top: 90px;
    display: flex; align-items: center; justify-content: center; gap: 14px;
    font-size: 56px; font-weight: 700;
  }
  .back-brand .brand-square { width: 26px; height: 26px; }
  .company-name {
    position: absolute;
    left: 0; right: 0; top: 200px;
    font-size: 46px; font-weight: 700;
    letter-spacing: 1.5px;
  }
  .licences {
    position: absolute;
    left: 0; right: 0; top: 346px;
    font-size: 24px;
  }
  .website {
    position: absolute;
    left: 0; right: 0; top: 381px;
    font-size: 23px;
    letter-spacing: 5.6px;
  }
</style>
</head>
<body>
  <section class="card card-front" aria-label="Business card front">
    <div class="front-brand"><span class="brand-square"></span>Tolvern</div>
    <div class="contact">
      <h1 class="person-name">Your Full Name</h1>
      <p class="person-title">Your Title</p>
      <ul class="detail-list">
        <li><span class="label">P</span>: 012-345-6786</li>
        <li><span class="label">M</span>: 012-345-6789</li>
        <li><span class="label">E</span>: your email address</li>
        <li class="gap"><span class="label">A</span>: Your address line 1</li>
        <li><span class="label"></span>&nbsp;&nbsp;Your address line 2</li>
        <li class="gap-lg"><span class="label">W</span>: www.tolvernsecurity.com.au</li>
      </ul>
    </div>
    <div class="front-band"></div>
  </section>

  <section class="card card-back" aria-label="Business card back">
    <div class="back-brand"><span class="brand-square"></span>Tolvern</div>
    <h2 class="company-name">TOLVERN SECURITY GROUP</h2>
    <p class="licences">Your licence number 1 &nbsp; / &nbsp;Your licence number 2</p>
    <p class="website">W: www.tolvernsecurity.com.au</p>
  </section>
</body>
</html>
```